Business Cards Design for the electrical wholesaler: clean bold dynamic :)

We need a business card design that would follow our latest brand guidelines. As an electrical wholesaler we want to bring a fresh look and feel into the industry. The design should be clean bold and dynamic. It should come alive with the renewed energy of our green colour. Our grey colour should keep things balanced and complement the notion of maturity and responsibility. We employ Lato as a corporate font however are not bound by this font and we’re open to interpretation here.

Target Market(s)

Electrical contractors

Industry/Entity Type

Business

Contact Information for Business Card

Logo
Name & Surname: Olena Dovbush
Job Title: Director of Marketing
Email: helen.dovbush@mailvane.example
Cell phone: XXX.XXX.XXXX
Address: 20917 - 87 Ave. Edmonton, AB, Canada. T6K 2R8
Business Phone: 780.555.0187
Website: www.qorvil.example

Font styles to use
Other font styles liked:
• Lato

Requirements
Must have
• Logo & website
Nice to have
• Brand elements - some of them you may find in the attached Brand Guidelines (e.g. three lines on the background signifying "W")

```html
<!DOCTYPE html>
<html lang="en">
<head>
<meta charset="utf-8">
<title>Qorvil business cards</title>
<link href="https://fonts.googleapis.com/css2?family=Lato:wght@400;700;900&display=swap" rel="stylesheet">
<style>
  :root {
    --green: #6bb43f;
    --charcoal: #3f4244;
    --charcoal-deep: #393c3e;
    --ink: #333638;
    --paper: #f2f2f0;
    --backdrop: #c9ccd3;
    --rule: #55585a;
    --light-text: #dcdcdc;
  }
  * { margin: 0; padding: 0; box-sizing: border-box; }
  html, body { width: 1200px; height: 952px; overflow: hidden; }
  body {
    background: var(--backdrop);
    font-family: "Lato", Arial, sans-serif;
    position: relative;
  }
  .card {
    position: absolute;
    width: 560px;
    height: 320px;
    border-radius: 4px;
  }
  .card-back {
    left: 60px;
    top: 110px;
    background: var(--charcoal);
    display: flex;
    align-items: center;
    justify-content: center;
  }
  .card-front {
    left: 580px;
    top: 500px;
    background: var(--paper);
  }
  .brand {
    display: flex;
    align-items: center;
    gap: 14px;
  }
  .brand-dot {
    width: 40px;
    height: 40px;
    border-radius: 50%;
    background: var(--green);
  }
  .brand-name {
    font-weight: 700;
    font-size: 66px;
    line-height: 1;
    letter-spacing: -1px;
  }
  .card-back .brand-name { color: var(--light-text); }
  .card-front .brand {
    position: absolute;
    right: 48px;
    top: 36px;
  }
  .card-front .brand-name { color: var(--ink); font-size: 60px; }
  .card-front .brand-dot { width: 36px; height: 36px; }
  .identity {
    position: absolute;
    left: 36px;
    top: 168px;
    width: 270px;
    color: var(--ink);
  }
  .person-name {
    color: var(--green);
    font-weight: 900;
    font-size: 22px;
    line-height: 1.1;
  }
  .person-title {
    font-size: 17px;
    color: #4a4d4f;
    margin-top: 2px;
  }
  .address {
    font-size: 17px;
    line-height: 1.3;
    margin-top: 22px;
    font-style: normal;
  }
  .divider {
    position: absolute;
    left: 300px;
    top: 150px;
    width: 1px;
    height: 120px;
    background: var(--rule);
  }
  .contacts {
    position: absolute;
    left: 314px;
    top: 146px;
    list-style: none;
    color: var(--ink);
    font-size: 15px;
  }
  .contacts li {
    display: flex;
    align-items: center;
    gap: 8px;
    height: 31px;
    white-space: nowrap;
  }
  .contacts svg { width: 18px; height: 18px; flex: none; }
  .contacts .email { font-size: 13.5px; }
</style>
</head>
<body>

<section class="card card-back" aria-label="Business card back">
  <div class="brand">
    <span class="brand-dot"></span>
    <span class="brand-name">qorvil</span>
  </div>
</section>

<section class="card card-front" aria-label="Business card front">
  <div class="brand">
    <span class="brand-dot"></span>
    <span class="brand-name">qorvil</span>
  </div>

  <div class="identity">
    <p class="person-name">Olena Dovbush</p>
    <p class="person-title">Director of Marketing</p>
    <address class="address">20917 - 87 Ave. Edmonton<br>AB Canada. T6K 2R8</address>
  </div>

  <div class="divider"></div>

  <ul class="contacts">
    <li>
      <svg viewBox="0 0 20 20" aria-hidden="true"><circle cx="10" cy="10" r="8.5" fill="none" stroke="#6bb43f" stroke-width="1.8"/><path d="M7 6c-.8.6-1 1.6-.5 2.8.8 1.9 2.6 3.8 4.6 4.7 1.1.5 2.1.3 2.7-.5l-1.6-1.5-1.2.6c-1-.5-2-1.5-2.5-2.5l.6-1.2z" fill="#6bb43f"/></svg>
      780.555.0187
    </li>
    <li>
      <svg viewBox="0 0 20 20" aria-hidden="true"><rect x="5.5" y="1.5" width="9" height="17" rx="1.5" fill="none" stroke="#3f4244" stroke-width="1.5"/><circle cx="10" cy="15.5" r="1" fill="#3f4244"/></svg>
      780.555.0342
    </li>
    <li class="email">
      <svg viewBox="0 0 20 20" aria-hidden="true"><rect x="1.5" y="4.5" width="17" height="11" fill="#6bb43f"/><path d="M1.5 4.5l8.5 6.5 8.5-6.5" fill="none" stroke="#f2f2f0" stroke-width="1.3"/></svg>
      helen.dovbush@mailvane.example
    </li>
    <li>
      <svg viewBox="0 0 20 20" aria-hidden="true"><circle cx="10" cy="10" r="8.5" fill="#6bb43f"/><path d="M1.5 10h17M10 1.5c-3 3-3 14 0 17M10 1.5c3 3 3 14 0 17" fill="none" stroke="#f2f2f0" stroke-width="1.1"/></svg>
      www.qorvil.example
    </li>
  </ul>
</section>

</body>
</html>
```